Telmoro Business Card

I already have the conplay logo. I need to develop a professional business card layout

Target Market(s)

Business

Industry/Entity Type

Business

Contact Information for Business Card

Company Name: Telmoro Limited

Font styles to use
Sans Serif

Colors

Designer to choose colors to be used in the design.

Requirements
Must have
• Use current logo
• Need two card size options:
• Small Card: 70mm x 28mm (Landscape)
• Square Card: 65mm x 65mm
Nice to have
• I will need 8-10 files for each name, number and email address (details to follow)

```html
<!DOCTYPE html>
<html lang="en">
<head>
<meta charset="utf-8">
<title>Telmoro Limited – Business Cards</title>
<link rel="stylesheet" href="https://fonts.googleapis.com/css2?family=Andika:wght@400;700&display=swap">
<style>
  :root {
    --navy: #2e2a7e;
    --ink: #1f1b6b;
    --brand: #1e7fc9;
    --paper: #ffffff;
    --stage: #f1f1f4;
    --tint-a: #eef5e6;
    --tint-b: #fdf1e2;
    --tint-c: #e8eef8;
  }
  * { box-sizing: border-box; margin: 0; padding: 0; }
  html, body {
    width: 1200px;
    height: 1063px;
    overflow: hidden;
  }
  body {
    position: relative;
    background: var(--stage);
    font-family: "Andika", "Trebuchet MS", sans-serif;
    color: var(--ink);
  }
  .band {
    position: absolute;
    left: 0; top: 0;
    width: 1200px; height: 460px;
    background: var(--navy);
  }
  .card {
    position: absolute;
    background: var(--paper);
    overflow: hidden;
  }
  .card-pattern {
    position: absolute;
    inset: 0;
    background: linear-gradient(120deg, var(--tint-a) 0%, var(--paper) 35%, var(--tint-b) 60%, var(--paper) 80%, var(--tint-c) 100%);
    opacity: 0.8;
  }
  .wordmark {
    position: absolute;
    font-weight: 700;
    color: var(--brand);
    letter-spacing: 0.02em;
    line-height: 1;
    white-space: nowrap;
  }

  /* Landscape card 70 x 28 mm */
  .card-small {
    left: 220px; top: 78px;
    width: 760px; height: 304px;
  }
  .card-small .address {
    position: absolute;
    top: 18px; left: 0; width: 100%;
    text-align: center;
    font-size: 19px;
  }
  .card-small .wordmark {
    left: 22px; top: 48px;
    font-size: 118px;
  }
  .card-small .company {
    position: absolute;
    left: 22px; top: 194px;
    font-size: 29px;
    line-height: 1.05;
  }
  .card-small .person {
    position: absolute;
    left: 22px; top: 228px;
    font-size: 19px;
  }
  .card-small .contact {
    position: absolute;
    right: 18px; top: 204px;
    text-align: right;
    font-size: 19px;
    line-height: 1.25;
  }

  /* Square card 65 x 65 mm */
  .card-square {
    left: 320px; top: 486px;
    width: 560px; height: 560px;
    box-shadow: 0 0 0 1px #dcdce4;
  }
  .card-square .wordmark {
    left: 0; width: 100%;
    top: 66px;
    text-align: center;
    font-size: 104px;
  }
  .card-square .details {
    position: absolute;
    left: 0; top: 238px; width: 100%;
    text-align: center;
    list-style: none;
    font-size: 36px;
    line-height: 1.13;
  }
</style>
</head>
<body>
  <div class="band"></div>

  <section class="card card-small" aria-label="Landscape business card">
    <div class="card-pattern" role="img" aria-label="Faint pastel repeat of the brand name behind the card content"></div>
    <p class="address">Address</p>
    <p class="wordmark">TELMORO</p>
    <p class="company">Telmoro Limited</p>
    <p class="person">Name</p>
    <p class="contact">Mobile<br>Email</p>
  </section>

  <section class="card card-square" aria-label="Square business card">
    <div class="card-pattern" role="img" aria-label="Faint pastel repeat of the brand name behind the card content"></div>
    <p class="wordmark">TELMORO</p>
    <ul class="details">
      <li>Telmoro Limited</li>
      <li>Name</li>
      <li>Address</li>
      <li>Mobile</li>
      <li>Email</li>
    </ul>
  </section>
</body>
</html>
```